Graphics for New Online Software

Looking at a designer to design a UI/UX Interface for an Online Events Platform (just JPEG) and some corresponding images for a website content (i.e. features etc)

Deliverables:
1x User Interface Design for the Platform (refer to attachment)
5-6x Feature Listing Images (refer to attachment)

Target Market(s)

Technology, Online Users Etc

Industry/Entity Type

Software Developer

Number of Pages Required

1 page

Font styles to use
Sans Serif

Colors
34a7d8
0493ce
3176b5
85acd3

Requirements
Must have
• Looks like a well built software - examples:
https://brivatel.io/
https://quornity.com/

All the images should look very professional, as though you are using it on the online platform itself.
Nice to have
• Refer to attached "Feature Listing" and Logo

```html
<!DOCTYPE html>
<html lang="en">
<head>
<meta charset="utf-8">
<title>Venuely – Online Events Platform</title>
<link href="https://fonts.googleapis.com/css2?family=Montserrat:wght@400;500;600;700;800&display=swap" rel="stylesheet">
<style>
:root{
  --bg:#eef3fa;
  --blue:#2c7fd6;
  --blue-dark:#1f62b0;
  --blue-light:#e3eefb;
  --blue-mid:#4a93e0;
  --navy:#15294d;
  --text:#1d2433;
  --muted:#7b8798;
  --line:#dfe6f0;
  --white:#fff;
}
*{box-sizing:border-box;margin:0;padding:0}
html,body{width:1200px;height:5137px;overflow:hidden}
body{background:var(--bg);font-family:'Montserrat',sans-serif;color:var(--text);position:relative}
.screen{position:absolute;left:120px;width:962px;background:var(--white);box-shadow:0 4px 18px rgba(40,80,140,.08);overflow:hidden}
.topbar{position:absolute;left:0;top:0;width:100%;height:98px}
.brand{position:absolute;left:30px;top:36px;font-size:19px;font-weight:800;color:var(--text);letter-spacing:-.5px;display:flex;align-items:center;gap:6px}
.brand i{width:12px;height:12px;background:var(--blue);display:inline-block}
.search{position:absolute;left:175px;top:34px;width:262px;height:28px;border:1px solid var(--line);border-radius:3px;font-size:9px;color:var(--muted);padding:8px 10px}
.search svg{position:absolute;right:10px;top:8px}
.duration{position:absolute;right:40px;top:41px;font-size:11px;color:var(--text);display:flex;align-items:center;gap:6px}
.duration b{font-weight:700}
.sidebar{position:absolute;left:0;top:98px;bottom:0;width:170px;background:var(--blue);color:#fff}
.sidebar ul{list-style:none;padding-top:24px}
.sidebar li{height:36px;line-height:36px;padding-left:30px;font-size:9.5px;font-weight:500;letter-spacing:.3px;position:relative}
.sidebar li.active{background:var(--blue-mid)}
.sidebar li.active::before{content:"";position:absolute;right:14px;top:13px;width:10px;height:10px;background:#fff;border-radius:2px}
.sidebar li.active::after{content:"";position:absolute;right:-6px;top:13px;border:5px solid transparent;border-left-color:var(--blue-mid)}
.sidebar .foot{position:absolute;left:30px;bottom:16px;font-size:7.5px;opacity:.9}
.title{position:absolute;font-size:20px;font-weight:700;color:var(--blue);letter-spacing:.5px}
.title::after{content:"";position:absolute;left:0;bottom:-6px;width:26px;height:3px;background:var(--blue)}
.ph{position:absolute;display:block}
.btn{display:inline-block;background:var(--blue);color:#fff;font-weight:600;border-radius:16px;font-size:9px;padding:6px 16px}
.small{font-size:8px;color:var(--muted);line-height:1.45}
.abs{position:absolute}
</style>
</head>
<body>

<!-- ============ SCREEN 1: EVENT INFO ============ -->
<section class="screen" style="top:60px;height:636px">
  <header class="topbar">
    <div class="brand"><i></i>VENUELY</div>
    <div class="search">Search<svg width="10" height="10" viewBox="0 0 10 10"><circle cx="4" cy="4" r="3" fill="none" stroke="#7b8798"/><path d="M6.5 6.5L9 9" stroke="#7b8798"/></svg></div>
    <div class="duration"><svg width="11" height="11" viewBox="0 0 12 12"><circle cx="6" cy="6" r="5" fill="none" stroke="#1d2433"/><path d="M6 3v3l2 1" stroke="#1d2433" fill="none"/></svg>EVENT DURATION : <b>2:00 HRS</b></div>
  </header>
  <nav class="sidebar"><ul><li class="active">EVENT INFO</li><li>STAGE</li><li>BREAKOUTS</li><li>BOOTHS</li><li>VIRTUAL EXHIBITION</li><li>REWARDS</li></ul><div class="foot">© 2020 www.venuely.com</div></nav>

  <h2 class="title" style="left:200px;top:102px">AGENDA</h2>
  <div class="ph" role="img" aria-label="Photo of a smiling conference speaker" style="left:200px;top:142px;width:292px;height:198px;background:linear-gradient(120deg,#3a3f4a,#8d95a3 60%,#dfe4ea)"></div>
  <div class="abs" style="left:340px;top:160px;width:146px;height:160px;background:var(--navy);color:#fff;padding:10px">
    <div style="background:var(--blue);border-radius:8px;font-size:6px;padding:3px 6px;text-align:center">June 25, 10:00AM to June 25 12:30 PM</div>
    <p style="font-size:7px;margin-top:10px">Preparing the programming interview:<br><b>Live Tips &amp; Portfolio Reviews</b></p>
    <p style="font-size:10px;font-weight:700;margin-top:14px">NORVANT</p>
    <p style="font-size:10px;font-weight:600;margin-top:6px">Career Fair</p>
    <p style="font-size:6px;opacity:.8">June 25, 10:00AM to June 25 12:30 PM</p>
  </div>
  <p class="abs" style="left:200px;top:360px;font-size:12px;font-weight:600">The Biggest Conference</p>

  <h2 class="title" style="left:518px;top:102px">PROGRAMMING</h2>
  <article class="abs" style="left:518px;top:142px;width:202px;height:232px;background:var(--blue-light);padding:16px 18px">
    <h3 style="font-size:10px;font-weight:700;line-height:1.3">VIVAMUS HABITANT CURSUS ADIPISCING SENECTUS.</h3>
    <p class="small" style="margin-top:8px">Duration : 2:00 Hrs</p>
    <p class="small" style="margin-top:4px;color:#444">Lorem ipsum dolor sit amet, has ad habeo tation delenit. An eam harum nonumy dolorum, sale dicat commodo mea ad. Sed cu legere ornatus.</p>
    <div class="ph" role="img" aria-label="Speaker portrait" style="left:18px;top:178px;width:40px;height:40px;border-radius:50%;background:linear-gradient(#8a6b58,#c9b3a3)"></div>
    <p class="abs" style="left:66px;top:184px;font-size:10px;font-weight:600">-Daicy</p>
    <p class="abs small" style="left:66px;top:200px">The Speaker</p>
  </article>
  <article class="abs" style="left:728px;top:142px;width:202px;height:232px;background:var(--blue-light);padding:16px 18px">
    <h3 style="font-size:10px;font-weight:700;line-height:1.3">PRIMIS ARCU HENDRERIT PURUS SENECTUS AENEAN MORBI</h3>
    <p class="small" style="margin-top:8px">Duration : 2:00 Hrs</p>
    <p class="small" style="margin-top:4px;color:#444">Lorem ipsum dolor sit amet, has ad habeo tation delenit. An eam harum nonumy dolorum, sale dicat commodo mea ad. Sed cu legere ornatus.</p>
    <div class="ph" role="img" aria-label="Speaker portrait" style="left:18px;top:178px;width:40px;height:40px;border-radius:50%;background:linear-gradient(#5a5048,#b8aca2)"></div>
    <p class="abs" style="left:66px;top:184px;font-size:10px;font-weight:600">-Merry</p>
    <p class="abs small" style="left:66px;top:200px">The Speaker</p>
  </article>

  <h2 class="title" style="left:200px;top:410px">SPEAKERS</h2>
  <div class="ph" role="img" aria-label="Speaker portrait of Linda" style="left:200px;top:462px;width:106px;height:106px;border-radius:50%;background:linear-gradient(#c9a27a,#e9ddd2)"></div>
  <div class="ph" role="img" aria-label="Speaker portrait of David" style="left:346px;top:462px;width:106px;height:106px;border-radius:50%;background:linear-gradient(#4a423c,#cbc3bb)"></div>
  <div class="ph" role="img" aria-label="Speaker portrait of Droid" style="left:492px;top:462px;width:106px;height:106px;border-radius:50%;background:linear-gradient(#6b5a4e,#d4c9c0)"></div>
  <div class="ph" role="img" aria-label="Speaker portrait of James" style="left:640px;top:462px;width:106px;height:106px;border-radius:50%;background:linear-gradient(#3b302b,#b8b0aa)"></div>
  <div class="ph" role="img" aria-label="Speaker portrait of Jhon" style="left:784px;top:462px;width:106px;height:106px;border-radius:50%;background:linear-gradient(#3d3a3a,#c2c4c8)"></div>
  <p class="abs" style="left:200px;top:578px;width:106px;text-align:center;font-size:12px;font-weight:600">LINDA</p>
  <p class="abs" style="left:346px;top:578px;width:106px;text-align:center;font-size:12px;font-weight:600">DAVID</p>
  <p class="abs" style="left:492px;top:578px;width:106px;text-align:center;font-size:12px;font-weight:600">DROID</p>
  <p class="abs" style="left:640px;top:578px;width:106px;text-align:center;font-size:12px;font-weight:600">JAMES</p>
  <p class="abs" style="left:784px;top:578px;width:106px;text-align:center;font-size:12px;font-weight:600">JHON</p>
</section>

<!-- ============ SCREEN 2: STAGE ============ -->
<section class="screen" style="top:740px;height:632px">
  <header class="topbar">
    <div class="brand"><i></i>VENUELY</div>
    <div class="search">Search<svg width="10" height="10" viewBox="0 0 10 10"><circle cx="4" cy="4" r="3" fill="none" stroke="#7b8798"/><path d="M6.5 6.5L9 9" stroke="#7b8798"/></svg></div>
    <div class="duration"><svg width="11" height="11" viewBox="0 0 12 12"><circle cx="6" cy="6" r="5" fill="none" stroke="#1d2433"/><path d="M6 3v3l2 1" stroke="#1d2433" fill="none"/></svg>EVENT DURATION : <b>2:00 HRS</b></div>
  </header>
  <nav class="sidebar"><ul><li>EVENT INFO</li><li class="active">STAGE</li><li>BREAKOUTS</li><li>BOOTHS</li><li>VIRTUAL EXHIBITION</li><li>REWARDS</li></ul><div class="foot">© 2020 www.venuely.com</div></nav>

  <h2 class="title" style="left:202px;top:82px">VIDEO</h2>
  <div class="ph" role="img" aria-label="Video still of a smiling woman presenting" style="left:202px;top:124px;width:502px;height:222px;background:linear-gradient(90deg,#9aa3ad,#e8ebef 70%,#f5f6f8);border-right:3px solid var(--navy);border-top:3px solid var(--navy)"></div>
  <p class="abs" style="left:478px;top:210px;font-size:13px;font-weight:600">The Biggest Conference</p>
  <div class="abs" style="left:478px;top:234px;display:flex;align-items:center;gap:8px;font-size:7.5px;color:var(--blue);font-weight:600"><svg width="24" height="24" viewBox="0 0 24 24"><circle cx="12" cy="12" r="12" fill="#2c7fd6"/><path d="M10 8l6 4-6 4z" fill="#fff"/></svg>Watch the video</div>

  <aside class="abs" style="left:724px;top:120px;width:186px;height:436px;background:var(--blue-light)">
    <div style="display:flex;font-size:9px;font-weight:600;height:24px;line-height:24px">
      <span style="background:var(--blue);color:#fff;padding:0 18px">CHAT</span><span style="padding:0 14px">Q&amp;A</span><span style="padding:0 8px">POLL</span>
    </div>
    <div style="padding:12px 10px;display:flex;flex-direction:column;gap:17px">
      <div style="display:flex;gap:8px"><span style="width:24px;height:24px;border-radius:50%;background:#b6a599;flex:none" role="img" aria-label="User avatar"></span><div style="flex:1"><p style="font-size:8px;color:var(--blue);font-weight:600;display:flex;justify-content:space-between">Jessika<span class="small" style="font-weight:400">6m ago</span></p><p class="small" style="font-size:6.5px">Secatis unde omnibens iste nat<br>fintaxlatisgalem accus</p></div></div>
      <div style="display:flex;gap:8px"><span style="width:24px;height:24px;border-radius:50%;background:#6f6258;flex:none" role="img" aria-label="User avatar"></span><div style="flex:1"><p style="font-size:8px;color:var(--blue);font-weight:600;display:flex;justify-content:space-between">Jhon Smith<span class="small" style="font-weight:400">6m ago</span></p><p class="small" style="font-size:6.5px">Secatis unde omnibens iste nat<br>fintaxlatisgalem accus</p></div></div>
      <div style="display:flex;gap:8px"><span style="width:24px;height:24px;border-radius:50%;background:#a08c7e;flex:none" role="img" aria-label="User avatar"></span><div style="flex:1"><p style="font-size:8px;color:var(--blue);font-weight:600;display:flex;justify-content:space-between">Desoka<span class="small" style="font-weight:400">6m ago</span></p><p class="small" style="font-size:6.5px">Secatis unde omnibens iste nat<br>fintaxlatisgalem accus</p></div></div>
      <div style="display:flex;gap:8px"><span style="width:24px;height:24px;border-radius:50%;background:#c2ae9e;flex:none" role="img" aria-label="User avatar"></span><div style="flex:1"><p style="font-size:8px;color:var(--blue);font-weight:600;display:flex;justify-content:space-between">Lorems<span class="small" style="font-weight:400">6m ago</span></p><p class="small" style="font-size:6.5px">Secatis unde omnibens iste nat<br>fintaxlatisgalem accus</p></div></div>
      <div style="display:flex;gap:8px"><span style="width:24px;height:24px;border-radius:50%;background:#a08c7e;flex:none" role="img" aria-label="User avatar"></span><div style="flex:1"><p style="font-size:8px;color:var(--blue);font-weight:600;display:flex;justify-content:space-between">Desoka<span class="small" style="font-weight:400">6m ago</span></p><p class="small" style="font-size:6.5px">Secatis unde omnibens iste nat<br>fintaxlatisgalem accus</p></div></div>
      <div style="display:flex;gap:8px"><span style="width:24px;height:24px;border-radius:50%;background:#c2ae9e;flex:none" role="img" aria-label="User avatar"></span><div style="flex:1"><p style="font-size:8px;color:var(--blue);font-weight:600;display:flex;justify-content:space-between">Lorems<span class="small" style="font-weight:400">6m ago</span></p><p class="small" style="font-size:6.5px">Secatis unde omnibens iste nat<br>fintaxlatisgalem accus</p></div></div>
    </div>
    <div class="abs" style="left:10px;bottom:12px;right:10px;display:flex;justify-content:space-between;align-items:center;font-size:8px;color:var(--muted);font-style:italic">Start Typing<span class="btn" style="font-style:normal;font-size:7px;padding:3px 10px">SEND</span></div>
  </aside>

  <h2 class="title" style="left:196px;top:382px">PROGRAMMING</h2>
  <div class="abs" style="left:196px;top:440px;display:flex;gap:10px">
    <article style="width:120px;height:116px;border:1px solid var(--line);padding:8px;text-align:center"><p style="font-size:6px;color:var(--blue)">09:00-09:30</p><div style="background:var(--blue-light);border-radius:14px;display:flex;align-items:center;gap:5px;padding:3px;margin-top:4px"><span style="width:20px;height:20px;border-radius:50%;background:#8d7b6e" role="img" aria-label="Speaker avatar"></span><span style="font-size:6.5px;font-weight:600;text-align:left">Jimemoon<br><span style="font-weight:400;font-size:5px">Secatis mirae</span></span></div><p class="small" style="font-size:6px;margin-top:8px">Secatis unde omnibens iste nat sitntaxlatisgalem accubiaciatis mous</p></article>
    <article style="width:120px;height:116px;border:1px solid var(--line);padding:8px;text-align:center"><p style="font-size:6px;color:var(--blue)">09:00-09:30</p><div style="background:var(--blue-light);border-radius:14px;display:flex;align-items:center;gap:5px;padding:3px;margin-top:4px"><span style="width:20px;height:20px;border-radius:50%;background:#b09a88" role="img" aria-label="Speaker avatar"></span><span style="font-size:6.5px;font-weight:600;text-align:left">Jimemoon<br><span style="font-weight:400;font-size:5px">Secatis mirae</span></span></div><p class="small" style="font-size:6px;margin-top:8px">Secatis unde omnibens iste nat sitntaxlatisgalem accubiaciatis mous</p></article>
    <article style="width:120px;height:116px;border:1px solid var(--line);padding:8px;text-align:center"><p style="font-size:6px;color:var(--blue)">09:00-09:30</p><div style="background:var(--blue-light);border-radius:14px;display:flex;align-items:center;gap:5px;padding:3px;margin-top:4px"><span style="width:20px;height:20px;border-radius:50%;background:#9b8678" role="img" aria-label="Speaker avatar"></span><span style="font-size:6.5px;font-weight:600;text-align:left">Jimemoon<br><span style="font-weight:400;font-size:5px">Secatis mirae</span></span></div><p class="small" style="font-size:6px;margin-top:8px">Secatis unde omnibens iste nat sitntaxlatisgalem accubiaciatis mous</p></article>
    <article style="width:120px;height:116px;border:1px solid var(--line);padding:8px;text-align:center"><p style="font-size:6px;color:var(--blue)">09:00-09:30</p><div style="background:var(--blue-light);border-radius:14px;display:flex;align-items:center;gap:5px;padding:3px;margin-top:4px"><span style="width:20px;height:20px;border-radius:50%;background:#6e625a" role="img" aria-label="Speaker avatar"></span><span style="font-size:6.5px;font-weight:600;text-align:left">Jimemoon<br><span style="font-weight:400;font-size:5px">Secatis mirae</span></span></div><p class="small" style="font-size:6px;margin-top:8px">Secatis unde omnibens iste nat sitntaxlatisgalem accubiaciatis mous</p></article>
  </div>
</section>

<!-- ============ SCREEN 3: BREAKOUTS ============ -->
<section class="screen" style="top:1420px;height:524px">
  <header class="topbar">
    <div class="brand"><i></i>VENUELY</div>
    <div class="search">Search<svg width="10" height="10" viewBox="0 0 10 10"><circle cx="4" cy="4" r="3" fill="none" stroke="#7b8798"/><path d="M6.5 6.5L9 9" stroke="#7b8798"/></svg></div>
    <div class="duration"><svg width="11" height="11" viewBox="0 0 12 12"><circle cx="6" cy="6" r="5" fill="none" stroke="#1d2433"/><path d="M6 3v3l2 1" stroke="#1d2433" fill="none"/></svg>EVENT DURATION : <b>2:00 HRS</b></div>
  </header>
  <nav class="sidebar" style="width:172px;top:90px"><ul><li>EVENT INFO</li><li>STAGE</li><li class="active">BREAKOUTS</li><li>BOOTHS</li><li>VIRTUAL EXHIBITION</li><li>REWARDS</li></ul><div class="foot">© 2020 www.venuely.com</div></nav>

  <div class="ph" role="img" aria-label="Empty meeting room photo" style="left:190px;top:90px;width:354px;height:196px;background:linear-gradient(160deg,#2c2f35,#5b6068 60%,#3a3d42)"></div>
  <div class="ph" role="img" aria-label="Empty meeting room photo" style="left:556px;top:90px;width:354px;height:196px;background:linear-gradient(160deg,#2a2d33,#62676e 60%,#36393e)"></div>
  <div class="ph" role="img" aria-label="Empty conference room photo" style="left:190px;top:300px;width:354px;height:194px;background:linear-gradient(160deg,#33363c,#6c7077 60%,#404348)"></div>
  <div class="ph" role="img" aria-label="Empty conference room photo" style="left:556px;top:300px;width:354px;height:194px;background:linear-gradient(160deg,#2d3035,#5e6269 60%,#3b3e43)"></div>

  <div class="abs" style="left:190px;top:156px;width:354px;text-align:center;color:#fff"><p style="font-size:15px;font-weight:700">JOIN BREAKOUT ROOM 1</p><p style="display:inline-block;background:var(--blue);color:#fff;font-weight:700;font-size:14px;padding:4px 12px;margin-top:10px;opacity:.9">3.00PM TO 4.30PM</p></div>
  <div class="abs" style="left:556px;top:156px;width:354px;text-align:center;color:#fff"><p style="font-size:15px;font-weight:700">JOIN BREAKOUT ROOM 2</p><p style="display:inline-block;background:var(--blue);color:#fff;font-weight:700;font-size:14px;padding:4px 12px;margin-top:10px;opacity:.9">3.00PM TO 4.30PM</p></div>
  <div class="abs" style="left:190px;top:364px;width:354px;text-align:center;color:#fff"><p style="font-size:15px;font-weight:700">JOIN BREAKOUT ROOM 3</p><p style="display:inline-block;background:var(--blue);color:#fff;font-weight:700;font-size:14px;padding:4px 12px;margin-top:10px;opacity:.9">3.00PM TO 4.30PM</p></div>
  <div class="abs" style="left:556px;top:364px;width:354px;text-align:center;color:#fff"><p style="font-size:15px;font-weight:700">JOIN BREAKOUT ROOM 4</p><p style="display:inline-block;background:var(--blue);color:#fff;font-weight:700;font-size:14px;padding:4px 12px;margin-top:10px;opacity:.9">3.00PM TO 4.30PM</p></div>

  <p class="abs" style="left:490px;top:262px;color:#fff;font-size:11px;font-weight:600">(4/50)</p>
  <p class="abs" style="left:850px;top:262px;color:#fff;font-size:11px;font-weight:600">(10/50)</p>
  <p class="abs" style="left:490px;top:470px;color:#fff;font-size:11px;font-weight:600">(4/50)</p>
  <p class="abs" style="left:850px;top:470px;color:#fff;font-size:11px;font-weight:600">(10/50)</p>
  <svg class="abs" style="left:512px;top:98px" width="22" height="22" viewBox="0 0 22 22"><circle cx="11" cy="11" r="11" fill="#fff"/><circle cx="10" cy="10" r="4" fill="none" stroke="#1d2433" stroke-width="1.5"/><path d="M13 13l3 3" stroke="#1d2433" stroke-width="1.5"/></svg>
  <svg class="abs" style="left:878px;top:98px" width="22" height="22" viewBox="0 0 22 22"><circle cx="11" cy="11" r="11" fill="#fff"/><circle cx="10" cy="10" r="4" fill="none" stroke="#1d2433" stroke-width="1.5"/><path d="M13 13l3 3" stroke="#1d2433" stroke-width="1.5"/></svg>
  <svg class="abs" style="left:512px;top:306px" width="22" height="22" viewBox="0 0 22 22"><circle cx="11" cy="11" r="11" fill="#fff"/><circle cx="10" cy="10" r="4" fill="none" stroke="#1d2433" stroke-width="1.5"/><path d="M13 13l3 3" stroke="#1d2433" stroke-width="1.5"/></svg>
  <svg class="abs" style="left:878px;top:306px" width="22" height="22" viewBox="0 0 22 22"><circle cx="11" cy="11" r="11" fill="#fff"/><circle cx="10" cy="10" r="4" fill="none" stroke="#1d2433" stroke-width="1.5"/><path d="M13 13l3 3" stroke="#1d2433" stroke-width="1.5"/></svg>
</section>

<!-- ============ SCREEN 4: BOOTHS ============ -->
<section class="screen" style="top:1996px;height:524px">
  <header class="topbar">
    <div class="brand"><i></i>VENUELY</div>
    <div class="search">Search<svg width="10" height="10" viewBox="0 0 10 10"><circle cx="4" cy="4" r="3" fill="none" stroke="#7b8798"/><path d="M6.5 6.5L9 9" stroke="#7b8798"/></svg></div>
    <div class="duration"><svg width="11" height="11" viewBox="0 0 12 12"><circle cx="6" cy="6" r="5" fill="none" stroke="#1d2433"/><path d="M6 3v3l2 1" stroke="#1d2433" fill="none"/></svg>EVENT DURATION : <b>2:00 HRS</b></div>
  </header>
  <nav class="sidebar" style="top:60px"><ul style="padding-top:40px"><li>EVENT INFO</li><li>STAGE</li><li>BREAKOUTS</li><li class="active">BOOTHS</li><li>VIRTUAL EXHIBITION</li><li>REWARDS</li></ul><div class="foot">© 2020 www.venuely.com</div></nav>

  <article class="abs" style="left:190px;top:80px;width:354px;height:184px;background:var(--blue-light);padding:10px 12px">
    <p style="font-size:9px;color:var(--blue);font-weight:600">SPONSOR - 1</p>
    <div style="background:#fff;margin-top:8px;height:140px;position:relative;padding:12px 18px">
      <p style="font-size:15px;font-weight:700">NORVANT</p>
      <span class="abs" style="right:18px;top:14px;background:var(--blue);color:#fff;border-radius:10px;font-size:6px;padding:4px 10px">June 25, 10:00AM to June 25 12:30 PM</span>
      <p style="font-size:11px;font-weight:600;margin-top:22px">Career Fair</p>
      <p class="small" style="font-size:7px">Preparing the programming interview:</p>
      <p style="font-size:7px;font-weight:600">Live Tips &amp; Portfolio Reviews</p>
      <span class="btn abs" style="right:30px;top:78px;font-size:7.5px">Find Out More</span>
    </div>
  </article>
  <article class="abs" style="left:556px;top:80px;width:354px;height:184px;background:var(--blue-light);padding:10px 12px">
    <p style="font-size:9px;color:var(--blue);font-weight:600">SPONSOR - 2</p>
    <div style="background:#fff;margin-top:8px;height:140px;position:relative;padding:12px 18px">
      <p style="font-size:15px;font-weight:700">HALDEN</p>
      <span class="abs" style="right:18px;top:14px;background:var(--blue);color:#fff;border-radius:10px;font-size:6px;padding:4px 10px">June 25, 10:00AM to June 25 12:30 PM</span>
      <p style="font-size:11px;font-weight:600;margin-top:22px">Career Fair</p>
      <p class="small" style="font-size:7px">Preparing the programming interview:</p>
      <p style="font-size:7px;font-weight:600">Live Tips &amp; Portfolio Reviews</p>
      <span class="btn abs" style="right:30px;top:78px;font-size:7.5px">Find Out More</span>
    </div>
  </article>
  <article class="abs" style="left:190px;top:278px;width:354px;height:184px;background:var(--blue-light);padding:10px 12px">
    <p style="font-size:9px;color:var(--blue);font-weight:600">SPONSOR - 3</p>
    <div style="background:#fff;margin-top:8px;height:140px;position:relative;padding:12px 18px">
      <p style="font-size:15px;font-weight:700">CIRQA</p>
      <span class="abs" style="right:18px;top:14px;background:var(--blue);color:#fff;border-radius:10px;font-size:6px;padding:4px 10px">June 25, 10:00AM to June 25 12:30 PM</span>
      <p style="font-size:11px;font-weight:600;margin-top:22px">Career Fair</p>
      <p class="small" style="font-size:7px">Preparing the programming interview:</p>
      <p style="font-size:7px;font-weight:600">Live Tips &amp; Portfolio Reviews</p>
      <span class="btn abs" style="right:30px;top:78px;font-size:7.5px">Find Out More</span>
    </div>
  </article>
  <article class="abs" style="left:556px;top:278px;width:354px;height:184px;background:var(--blue-light);padding:10px 12px">
    <p style="font-size:9px;color:var(--blue);font-weight:600">SPONSOR - 4</p>
    <div style="background:#fff;margin-top:8px;height:140px;position:relative;padding:12px 18px">
      <p style="font-size:15px;font-weight:700">TELMOR</p>
      <span class="abs" style="right:18px;top:14px;background:var(--blue);color:#fff;border-radius:10px;font-size:6px;padding:4px 10px">June 25, 10:00AM to June 25 12:30 PM</span>
      <p style="font-size:11px;font-weight:600;margin-top:22px">Career Fair</p>
      <p class="small" style="font-size:7px">Preparing the programming interview:</p>
      <p style="font-size:7px;font-weight:600">Live Tips &amp; Portfolio Reviews</p>
      <span class="btn abs" style="right:30px;top:78px;font-size:7.5px">Find Out More</span>
    </div>
  </article>
</section>

<!-- ============ SCREEN 5: VIRTUAL EXHIBITION ============ -->
<section class="screen" style="top:2570px;height:530px">
  <header class="topbar">
    <div class="brand"><i></i>VENUELY</div>
    <div class="search">Search<svg width="10" height="10" viewBox="0 0 10 10"><circle cx="4" cy="4" r="3" fill="none" stroke="#7b8798"/><path d="M6.5 6.5L9 9" stroke="#7b8798"/></svg></div>
    <div class="duration"><svg width="11" height="11" viewBox="0 0 12 12"><circle cx="6" cy="6" r="5" fill="none" stroke="#1d2433"/><path d="M6 3v3l2 1" stroke="#1d2433" fill="none"/></svg>EVENT DURATION : <b>2:00 HRS</b></div>
  </header>
  <nav class="sidebar" style="top:68px"><ul style="padding-top:36px"><li>EVENT INFO</li><li>STAGE</li><li>BREAKOUTS</li><li>BOOTHS</li><li class="active">VIRTUAL EXHIBITION</li><li>REWARDS</li></ul><div class="foot">© 2020 www.venuely.com</div></nav>

  <div class="ph" role="img" aria-label="Isometric illustration of virtual exhibition booths with visitors" style="left:234px;top:86px;width:630px;height:368px;background:radial-gradient(ellipse at center,#cfe0f6 0%,#eef3fb 55%,#f7f9fc 100%);border:1px solid var(--line)"></div>
  <svg class="abs" style="left:532px;top:252px" width="34" height="34" viewBox="0 0 34 34"><circle cx="17" cy="17" r="17" fill="#111"/><path d="M13 10l11 7-11 7z" fill="#fff"/></svg>
  <p class="abs" style="left:234px;top:474px;font-size:9px">Lorem ipsum dolor sit amet, consectetur adipiscing elit, sed do eiusmod</p>
  <p class="abs" style="left:234px;top:488px;font-size:9px;color:var(--blue);font-weight:600;text-decoration:underline">Click Here</p>
  <span class="btn abs" style="left:754px;top:476px;font-size:10px;padding:8px 16px">Find Out More</span>
</section>

<!-- ============ SCREEN 6: REWARDS ============ -->
<section class="screen" style="top:3140px;height:400px">
  <header class="topbar">
    <div class="brand"><i></i>VENUELY</div>
    <div class="search">Search<svg width="10" height="10" viewBox="0 0 10 10"><circle cx="4" cy="4" r="3" fill="none" stroke="#7b8798"/><path d="M6.5 6.5L9 9" stroke="#7b8798"/></svg></div>
    <div class="duration"><svg width="11" height="11" viewBox="0 0 12 12"><circle cx="6" cy="6" r="5" fill="none" stroke="#1d2433"/><path d="M6 3v3l2 1" stroke="#1d2433" fill="none"/></svg>EVENT DURATION : <b>2:00 HRS</b></div>
  </header>
  <nav class="sidebar" style="top:68px"><ul style="padding-top:40px"><li>EVENT INFO</li><li>STAGE</li><li>BREAKOUTS</li><li>BOOTHS</li><li>VIRTUAL EXHIBITION</li><li class="active">REWARDS</li></ul><div class="foot">© 2020 www.venuely.com</div></nav>

  <div class="abs" style="left:256px;top:110px;width:584px;height:230px;background:var(--blue-light)">
    <ul style="list-style:none;position:absolute;left:70px;top:46px;display:flex;flex-direction:column;gap:16px;font-size:11px;font-weight:600">
      <li style="color:var(--blue);display:flex;gap:10px;align-items:center"><svg width="10" height="10" viewBox="0 0 10 10"><path d="M1 1l4 4-4 4M5 1l4 4-4 4" fill="none" stroke="#2c7fd6" stroke-width="1.4"/></svg>Visited Virtual Exhibition</li>
      <li style="display:flex;gap:10px;align-items:center"><svg width="10" height="10" viewBox="0 0 10 10"><path d="M1 1l4 4-4 4M5 1l4 4-4 4" fill="none" stroke="#2c7fd6" stroke-width="1.4"/></svg>Joined Breakout Room</li>
      <li style="display:flex;gap:10px;align-items:center"><svg width="10" height="10" viewBox="0 0 10 10"><path d="M1 1l4 4-4 4M5 1l4 4-4 4" fill="none" stroke="#2c7fd6" stroke-width="1.4"/></svg>Checked out Booths</li>
    </ul>
    <span class="btn abs" style="left:72px;top:148px;font-size:10px;padding:7px 16px">Claim Reward</span>
    <svg class="abs" style="left:386px;top:56px" width="120" height="120" viewBox="0 0 120 120"><circle cx="60" cy="60" r="56" fill="#fff"/><circle cx="60" cy="60" r="56" fill="none" stroke="#1f3a8a" stroke-width="4"/><path d="M60 4a56 56 0 0 1 56 56" fill="none" stroke="#2c7fd6" stroke-width="4"/><text x="60" y="66" text-anchor="middle" font-family="Montserrat,sans-serif" font-size="18" font-weight="600" fill="#1d2433">40/100</text></svg>
  </div>
</section>

<!-- ============ SCREEN 7: EVENTS LIST ============ -->
<section class="screen" style="top:3586px;height:924px">
  <header class="topbar">
    <div class="brand"><i></i>VENUELY</div>
    <div class="search">Search<svg width="10" height="10" viewBox="0 0 10 10"><circle cx="4" cy="4" r="3" fill="none" stroke="#7b8798"/><path d="M6.5 6.5L9 9" stroke="#7b8798"/></svg></div>
    <div class="duration"><svg width="11" height="11" viewBox="0 0 12 12"><circle cx="6" cy="6" r="5" fill="none" stroke="#1d2433"/><path d="M6 3v3l2 1" stroke="#1d2433" fill="none"/></svg>EVENT DURATION : <b>2:00 HRS</b></div>
  </header>
  <nav class="sidebar" style="top:60px"><ul style="padding-top:44px"><li>EVENT INFO</li><li>STAGE</li><li>BREAKOUTS</li><li>BOOTHS</li><li>VIRTUAL EXHIBITION</li><li>REWARDS</li></ul><div class="foot">© 2020 www.venuely.com</div></nav>

  <div class="ph" role="img" aria-label="Photo of a presenter pointing at a screen in a meeting" style="left:180px;top:86px;width:736px;height:178px;background:linear-gradient(90deg,#2d3138,#5f656e 50%,#9aa0a8)"></div>
  <p class="abs" style="left:202px;top:186px;color:#fff;font-size:20px;font-weight:600">Events List</p>
  <p class="abs" style="left:202px;top:214px;color:#dfe4ea;font-size:8px">In hac habitasse platea dictumst, nisi sit amet sed eget dui viverra scelerisque.</p>

  <div class="abs" style="left:196px;top:296px;display:flex;gap:20px;font-size:7px;font-weight:600">
    <div><p>Search Event</p><div style="width:136px;height:20px;border:1px solid var(--line);margin-top:6px"></div></div>
    <div><p>Select Category</p><div style="width:130px;height:20px;border:1px solid var(--line);margin-top:6px;font-weight:400;color:var(--muted);padding:5px 6px;display:flex;justify-content:space-between">All Category<span>▾</span></div></div>
    <div><p>Search By Location City</p><div style="display:flex;gap:6px;margin-top:6px"><div style="width:116px;height:20px;border:1px solid var(--line);font-weight:400;color:var(--muted);padding:5px 6px">Type a venue city name...</div><span style="border:1px solid var(--blue);color:var(--blue);border-radius:10px;padding:5px 8px;font-size:6.5px">RESET</span><span style="background:var(--blue);color:#fff;border-radius:10px;padding:5px 8px;font-size:6.5px">OK</span></div></div>
  </div>

  <div class="abs" style="left:180px;top:384px;display:grid;grid-template-columns:repeat(3,176px);gap:20px 20px">
    <article style="height:230px;border:1px solid var(--line)"><div role="img" aria-label="Photo of a speaker on stage" style="height:108px;background:linear-gradient(#4f6c94,#a7b9cf)"></div><div style="padding:14px 20px"><p style="font-size:8px;font-weight:600">Events Ebook</p><p class="small" style="font-size:7px;margin-top:12px">24 September 2015<br>◷ 08:00am - 05:00pm<br>● Leslie Hall Sibsea</p></div></article>
    <article style="height:230px;border:1px solid var(--line)"><div role="img" aria-label="Photo of a man presenting at a podium" style="height:108px;background:linear-gradient(#5b5f66,#b0b4b9)"></div><div style="padding:14px 20px"><p style="font-size:8px;font-weight:600">Festival of Praise</p><p class="small" style="font-size:7px;margin-top:12px">24 September 2015<br>◷ 08:00am - 05:00pm<br>● Avalon Industrial Park</p></div></article>
    <article style="height:230px;border:1px solid var(--line)"><div role="img" aria-label="Photo of a presenter with a headset" style="height:108px;background:linear-gradient(#2f3238,#8a8e95)"></div><div style="padding:14px 20px"><p style="font-size:8px;font-weight:600">Quick Ways to Make a<br>Great Event Page</p><p class="small" style="font-size:7px;margin-top:6px">24 September 2015<br>◷ 08:00am - 05:00pm<br>● Belmont Lower Hall</p></div></article>
    <article style="height:236px;border:1px solid var(--line)"><div role="img" aria-label="Photo of business people walking" style="height:108px;background:linear-gradient(#3a3c40,#c3c5c8)"></div><div style="padding:14px 20px"><p style="font-size:8px;font-weight:600">Events Ebook</p><p class="small" style="font-size:7px;margin-top:12px">24 September 2015<br>◷ 08:00am - 05:00pm<br>● Leslie Hall Sibsea</p></div></article>
    <article style="height:236px;border:1px solid var(--line)"><div role="img" aria-label="Photo of a concert crowd under stage lights" style="height:108px;background:linear-gradient(#1d1f6b,#8a3fc0 60%,#2c7fd6)"></div><div style="padding:14px 20px"><p style="font-size:8px;font-weight:600">Festival of Praise</p><p class="small" style="font-size:7px;margin-top:12px">24 September 2015<br>◷ 08:00am - 05:00pm<br>● Avalon Industrial Park</p></div></article>
    <article style="height:236px;border:1px solid var(--line)"><div role="img" aria-label="Photo of a speaker presenting in a dark room" style="height:108px;background:linear-gradient(#1e2024,#6b3c3c 70%,#3a3c42)"></div><div style="padding:14px 20px"><p style="font-size:8px;font-weight:600">Quick Ways to Make a<br>Great Event Page</p><p class="small" style="font-size:7px;margin-top:6px">24 September 2015<br>◷ 08:00am - 05:00pm<br>● Belmont Lower Hall</p></div></article>
  </div>

  <aside class="abs" style="left:764px;top:284px;width:146px">
    <p style="font-size:7px;font-weight:700">EVENTS CALENDAR</p>
    <div style="border:1px solid var(--line);margin-top:8px;padding:4px">
      <div style="background:var(--blue);color:#fff;font-size:6.5px;display:flex;justify-content:space-between;padding:3px 5px"><span>« ‹</span><span>June 2020</span><span>› »</span></div>
      <div style="display:grid;grid-template-columns:repeat(7,1fr);font-size:6px;text-align:center;row-gap:5px;margin-top:5px;color:var(--text)">
        <b>S</b><b>M</b><b>T</b><b>W</b><b>T</b><b>F</b><b>S</b>
        <span>31</span><span>1</span><span>2</span><span>3</span><span>4</span><span>5</span><span>6</span>
        <span>7</span><span>8</span><span>9</span><span>10</span><span>11</span><span>12</span><span>13</span>
        <span>14</span><span>15</span><span>16</span><span>17</span><span>18</span><span style="background:var(--blue);color:#fff">19</span><span>20</span>
        <span>21</span><span>22</span><span>23</span><span>24</span><span>25</span><span>26</span><span>27</span>
        <span>28</span><span>29</span><span>30</span><span>1</span><span>2</span><span>3</span><span>4</span>
      </div>
    </div>
    <p style="font-size:7px;font-weight:700;margin-top:26px">EVENTS LEGEND</p>
    <ul style="list-style:none;border:1px solid var(--line);margin-top:8px;padding:8px 10px;font-size:6.5px;color:var(--muted);display:flex;flex-direction:column;gap:10px">
      <li>▪ DEFAULT</li><li>▪ Location Events</li><li>▪ Social Media</li><li>▪ Planing</li><li>▪ Technology</li><li>▪ Ebooks</li><li>▪ Entertainment</li><li>▪ All Categories</li>
    </ul>
  </aside>

  <p class="abs" style="left:434px;top:890px;font-size:7px;color:var(--muted)">Loading <svg width="12" height="12" viewBox="0 0 12 12" style="vertical-align:middle"><circle cx="6" cy="6" r="4.5" fill="none" stroke="#2c7fd6" stroke-dasharray="3 2"/></svg></p>
</section>

<!-- ============ SCREEN 8: REGISTER ============ -->
<section class="screen" style="top:4546px;height:550px">
  <header class="topbar">
    <div class="brand"><i></i>VENUELY</div>
    <div class="search">Search<svg width="10" height="10" viewBox="0 0 10 10"><circle cx="4" cy="4" r="3" fill="none" stroke="#7b8798"/><path d="M6.5 6.5L9 9" stroke="#7b8798"/></svg></div>
    <div class="duration"><svg width="11" height="11" viewBox="0 0 12 12"><circle cx="6" cy="6" r="5" fill="none" stroke="#1d2433"/><path d="M6 3v3l2 1" stroke="#1d2433" fill="none"/></svg>EVENT DURATION : <b>2:00 HRS</b></div>
  </header>
  <nav class="sidebar" style="top:62px"><ul style="padding-top:40px"><li>EVENT INFO</li><li>STAGE</li><li>BREAKOUTS</li><li>BOOTHS</li><li>VIRTUAL EXHIBITION</li><li class="active">REWARDS</li></ul><div class="foot">© 2020 www.venuely.com</div></nav>

  <div class="abs" style="left:256px;top:94px;width:350px;height:304px;background:#fff;border:1px solid var(--line);padding:18px 28px">
    <p style="display:flex;align-items:center;gap:8px;font-size:10px;color:var(--blue);font-weight:600"><svg width="18" height="18" viewBox="0 0 18 18"><rect x="1.5" y="3" width="15" height="13" fill="none" stroke="#1d2433" stroke-width="1.4"/><path d="M1.5 7h15M5 1v4M13 1v4" stroke="#1d2433" stroke-width="1.4"/></svg>REGISTER</p>
    <h3 style="font-size:11px;font-weight:700;margin-top:28px;line-height:1.3">Live Webinar : Grow Your Audieance<br>And Boost Conversions...</h3>
    <p style="font-size:7px;font-weight:600;margin-top:8px">During the webinar you'll learn secrets to these key Questions:</p>
    <ul style="list-style:none;font-size:7px;line-height:1.5;color:#444;margin-top:12px;display:flex;flex-direction:column;gap:14px">
      <li style="display:flex;gap:8px"><span style="color:var(--blue)">✓</span>Lorem ipsum dolor sit amet, vim justo aliquip qualisque ut, eum ne tollit iisque, at mel integre mentitum delectus.</li>
      <li style="display:flex;gap:8px"><span style="color:var(--blue)">✓</span>Cu qui illum scripta. Ei duo quot laudem nostro. Ei duo etiam otiuperatis no illud ipsum</li>
      <li style="display:flex;gap:8px"><span style="color:var(--blue)">✓</span>An vidit malis mentitum cum, partem splendide his in, quo dolore doming ex. Facilisi detracto</li>
    </ul>
  </div>
  <div class="abs" style="left:606px;top:94px;width:256px;height:304px;background:var(--blue-light);padding:18px 24px">
    <p style="font-size:12px;font-weight:600;color:var(--blue)">Register for the Webinar</p>
    <div class="ph" role="img" aria-label="Presenter portrait" style="left:24px;top:52px;width:50px;height:50px;border-radius:50%;background:linear-gradient(#5a4e46,#c0b5ac)"></div>
    <p class="abs" style="left:86px;top:62px;font-size:12px;font-weight:600;line-height:1.2">Presented by<br>Droid</p>
    <p class="small abs" style="left:24px;top:120px;width:210px;font-size:7.5px;color:#444">Lorem ipsum dolor sit amet, vim justo aliquip qualisque ut, eum ne tollit iisque, at mel integre mentitum delectus. Cu qui illum scripta.</p>
    <p class="abs" style="left:24px;top:178px;font-size:8px;color:var(--blue);font-weight:600">DATE : <span style="color:var(--text)">JUNE 02, 2020</span></p>
    <p class="abs" style="left:24px;top:206px;font-size:8px;color:var(--blue);font-weight:600">TIME : <span style="color:var(--text)">1 PM (EST)</span></p>
    <p class="small abs" style="left:24px;top:222px;width:210px;font-size:5.5px">If you register and cannot attend, don't worry, we will send you a full recording the day after the webinar</p>
    <span class="btn abs" style="left:36px;top:258px;font-size:10px;padding:8px 20px">REGISTER YOUR SPOT ›</span>
  </div>
  <div class="abs" style="left:256px;top:398px;width:606px;height:132px;background:#15161a;color:#fff;display:flex;align-items:center;gap:24px;padding:0 26px">
    <svg width="42" height="38" viewBox="0 0 42 38" style="flex:none"><path d="M21 2L40 36H2z" fill="#2c7fd6"/><path d="M21 14v11" stroke="#15161a" stroke-width="4"/><circle cx="21" cy="30" r="2.4" fill="#15161a"/></svg>
    <p style="font-size:7px;line-height:1.7;font-style:italic"><b>IMPORTANT :</b> Seats for this live session are limited and are given on a first come, first served basis. Please join a few minutes early to test your audio and video settings. Neque porro quisquam est qui dolorem ipsum quia dolor sit amet, consectetur, adipisci</p>
  </div>
</section>

</body>
</html>
```